ultra-minimalist business card

front (black background, matte):

tarik b. hosseny
writer | photographer
get@tarikhosseny.com

back (white background, matte):

a picture speaks a thousand words;
a word draws a thousand pictures.

www.tarikhosseny.com

all text should be small (white or silver - as long as it shows against the black - on the front; black or gray - as long as it shows against the white - on the back).

feel free to get creative in terms of arrangement, alignment, and font type, but remember, the overall style is minimalist, so nothing too fancy, please.

thanks.

```html
<!DOCTYPE html>
<html lang="en">
<head>
<meta charset="utf-8">
<title>Tarik B. Hosseny — Business Card</title>
<link rel="stylesheet" href="https://fonts.googleapis.com/css2?family=Oswald:wght@300;400&family=Open+Sans:wght@400;700&display=swap">
<style>
  :root {
    --stage: #bfbfbf;
    --card-white: #ffffff;
    --card-black: #1f1d1d;
    --ink-black: #1a1a1a;
    --ink-white: #ffffff;
    --ink-gray: #8a8a8a;
    --card-shadow: 0 10px 30px rgba(0, 0, 0, 0.25);
  }
  * { margin: 0; padding: 0; box-sizing: border-box; }
  html, body {
    width: 1200px;
    height: 800px;
    overflow: hidden;
    background: var(--stage);
  }
  .stage {
    position: relative;
    width: 1200px;
    height: 800px;
    display: flex;
    align-items: center;
    justify-content: center;
    gap: 60px;
  }
  .card {
    position: relative;
    width: 520px;
    height: 300px;
    border-radius: 3px;
    box-shadow: var(--card-shadow);
  }
  .card--back { background: var(--card-white); }
  .card--front { background: var(--card-black); }

  .quote {
    position: absolute;
    left: 48px;
    top: 46px;
    font-family: "Oswald", sans-serif;
    font-weight: 400;
    font-size: 40px;
    line-height: 1.02;
    letter-spacing: -0.5px;
    color: var(--ink-black);
    transform: scaleX(0.82);
    transform-origin: left top;
    white-space: nowrap;
  }
  .website {
    position: absolute;
    right: 40px;
    bottom: 36px;
    font-family: "Open Sans", sans-serif;
    font-size: 15px;
    color: var(--ink-black);
  }

  .identity {
    position: absolute;
    left: 300px;
    top: 196px;
    font-family: "Open Sans", sans-serif;
    color: var(--ink-white);
  }
  .identity__name {
    font-weight: 700;
    font-size: 17px;
    line-height: 1.3;
  }
  .identity__role {
    font-size: 10.5px;
    letter-spacing: 0.6px;
    text-transform: uppercase;
    color: var(--ink-gray);
    line-height: 1.7;
  }
  .identity__email {
    font-size: 15px;
    line-height: 1.4;
  }
</style>
</head>
<body>
  <main class="stage">
    <section class="card card--back" aria-label="Card back">
      <p class="quote">“a picture speaks a thousand words,<br>a word draws a thousand pictures. ”</p>
      <p class="website">www.tarikhosseny.com</p>
    </section>
    <section class="card card--front" aria-label="Card front">
      <div class="identity">
        <p class="identity__name">tarik b. hosseny</p>
        <p class="identity__role">writer | photographer</p>
        <p class="identity__email">get@tarikhosseny.com</p>
      </div>
    </section>
  </main>
</body>
</html>
```